Vital Spark Electrical in need of a business card design

We need a new business card designed for our electrical business. We have a logo already which I will attach below.
Would like the business card to be..
-BLACK background preferably, possibly white back ground behind logo if colours clash.
-White & Blue (logo blue) text
Something that makes the logo pop, & a modern look. Possibly minimal clean format.

REQUIRE:
-Logo on front & back

TEXT TO INCLUDE (ON ONE SIDE):

Tom Harlow
Director/Electrician
M: 0417 365 208
E:info@vitalsparkelectrical-example.com.au
W:www.vitalsparkelectrical-example.com.au
R.E.C 57318

Custom/New Homes
Renovations
Commercial Office/Shop Fit-outs
Communications & Security Cameras
Electric Vehicle Chargers
Airconditioning
Updates

Requirements
Nice to have
• Possibly even lighten the grey shades for the words 'Vital' & 'Spark' to be more easily read on a black background.

```html
<!DOCTYPE html>
<html lang="en">
<head>
<meta charset="utf-8">
<title>Vital Spark Electrical — Business Card</title>
<link href="https://fonts.googleapis.com/css2?family=Pathway+Gothic+One&display=swap" rel="stylesheet">
<style>
  :root {
    --page-bg: #dce8f8;
    --card-front: #050709;
    --card-back: #1a1b1d;
    --plate-fill: #1b1c1f;
    --plate-border: #3a4047;
    --brand-blue: #1aa3e0;
    --text-white: #f2f3f4;
    --text-grey: #9ea2a8;
  }
  * { margin: 0; padding: 0; box-sizing: border-box; }
  html, body {
    width: 1200px; height: 1200px; overflow: hidden;
    background: var(--page-bg);
    font-family: "Pathway Gothic One", "Arial Narrow", sans-serif;
  }
  .canvas { position: relative; width: 1200px; height: 1200px; }
  .card {
    position: absolute; left: 180px; width: 840px; height: 480px;
    border-radius: 40px; overflow: hidden;
  }
  .card--front { top: 56px; background: var(--card-front); }
  .card--back { top: 632px; background: var(--card-back); }

  .brand-plate {
    position: absolute; left: 224px; top: 160px; width: 392px; height: 158px;
    border: 2px solid var(--plate-border); border-radius: 22px;
    background: var(--plate-fill);
    display: flex; align-items: center; justify-content: center;
  }
  .brand-name {
    color: var(--text-white); font-size: 40px; letter-spacing: 1px;
    white-space: nowrap;
  }

  .services {
    position: absolute; right: 441px; top: 0; text-align: right;
    list-style: none; color: var(--text-white); font-size: 25px; line-height: 1;
  }
  .services li { position: absolute; right: 0; white-space: nowrap; }

  .divider {
    position: absolute; left: 0; top: 0; width: 840px; height: 480px;
  }

  .contact {
    position: absolute; left: 440px; top: 0; color: var(--text-white);
    font-size: 25px; line-height: 1;
  }
  .contact > * { position: absolute; left: 0; white-space: nowrap; }
  .contact__name { color: var(--brand-blue); font-size: 32px; }
  .contact__role { color: var(--text-grey); }
  .contact__label { color: var(--brand-blue); }

  .brand-corner {
    position: absolute; right: 30px; bottom: 34px;
    color: var(--text-white); font-size: 20px; letter-spacing: 0.5px;
  }
</style>
</head>
<body>
<main class="canvas">
  <section class="card card--front" aria-label="Card front">
    <div class="brand-plate">
      <span class="brand-name">Vital Spark Electrical</span>
    </div>
  </section>

  <section class="card card--back" aria-label="Card back">
    <ul class="services">
      <li style="top:135px">Custom/New Homes</li>
      <li style="top:169px">Renovations</li>
      <li style="top:208px">Commercial Office/Shop Fit-outs</li>
      <li style="top:243px">Communications &amp; Security Cameras</li>
      <li style="top:279px">Electric Vehicle Chargers</li>
      <li style="top:316px">Airconditioning</li>
    </ul>

    <svg class="divider" viewBox="0 0 840 480" aria-hidden="true">
      <line x1="418" y1="96" x2="421" y2="382" stroke="#f2f3f4" stroke-width="2"/>
    </svg>

    <div class="contact">
      <p class="contact__name" style="top:141px">Tom Harlow</p>
      <p class="contact__role" style="top:173px">Director/Electrician</p>
      <p style="top:209px"><span class="contact__label">M:</span> 0417 365 208</p>
      <p style="top:245px"><span class="contact__label">E:</span> info@vitalsparkelectrical-example.com.au</p>
      <p style="top:281px"><span class="contact__label">W:</span> www.vitalsparkelectrical-example.com.au</p>
      <p style="top:317px">R.E.C 57318</p>
    </div>

    <span class="brand-corner">Vital Spark Electrical</span>
  </section>
</main>
</body>
</html>
```